TideForge, LLC
Business Cards - Consulting
Business Cards
Professional
Desmond K Harlow
President
318 Quillfeather Court Brownsburg, IN 46219
dharlow4872@mailnest.example

```html
<!DOCTYPE html>
<html lang="en">
<head>
<meta charset="utf-8">
<title>TideForge, LLC – Stationery Set</title>
<link rel="stylesheet" href="https://fonts.googleapis.com/css2?family=Montserrat:wght@400;600;800&display=swap">
<style>
  :root {
    --stage: #8b8d90;
    --stage-light: #a3a5a8;
    --paper: #ffffff;
    --navy: #2f4868;
    --brand: #3c9a48;
    --ink: #4a4f57;
    --faint: #eef1ee;
    --faint-line: #dfe5e0;
  }
  * { margin: 0; padding: 0; box-sizing: border-box; }
  html, body { width: 1200px; height: 626px; overflow: hidden; }
  body {
    background: radial-gradient(ellipse at 50% 40%, var(--stage-light), var(--stage) 75%);
    font-family: "Montserrat", sans-serif;
    color: var(--ink);
    position: relative;
  }
  .sheet { position: absolute; background: var(--paper); overflow: hidden; }

  .brand {
    display: flex; align-items: center; justify-content: center; gap: 5px;
    font-weight: 800; color: var(--brand); letter-spacing: 0.2px; white-space: nowrap;
  }
  .brand-dot { border-radius: 50%; background: var(--navy); flex: none; }

  /* Business card front */
  .card-front { left: 34px; top: 192px; width: 187px; height: 106px; border-radius: 6px; }
  .card-front .brand { position: absolute; left: 0; right: 0; top: 40px; font-size: 13px; }
  .card-front .brand-dot { width: 14px; height: 14px; }

  /* Business card back */
  .card-back { left: 34px; top: 307px; width: 187px; height: 106px; border-radius: 6px; }
  .card-back .band { height: 11px; background: var(--navy); }
  .card-back .brand { margin-top: 10px; font-size: 11px; }
  .card-back .brand-dot { width: 12px; height: 12px; }
  .card-back .person { text-align: center; margin-top: 9px; }
  .card-back .name { font-size: 6px; font-weight: 600; }
  .card-back .title { font-size: 5px; margin-top: 2px; }
  .card-back .contact { position: absolute; left: 4px; right: 4px; bottom: 8px; text-align: center; font-size: 3.6px; white-space: nowrap; }

  /* Letterhead */
  .letterhead { left: 233px; top: 31px; width: 365px; height: 569px; }
  .letterhead .band { height: 19px; background: var(--navy); }
  .letterhead .notch { position: absolute; left: 172px; top: 4px; width: 22px; height: 22px; border-radius: 50%; background: var(--paper); }
  .letterhead .brand { position: absolute; left: 0; right: 0; top: 60px; font-size: 15px; }
  .letterhead .brand-dot { width: 15px; height: 15px; }
  .letterhead .mark { position: absolute; left: 105px; top: 175px; width: 215px; height: 215px; }
  .letterhead .contact { position: absolute; left: 0; right: 0; bottom: 32px; text-align: center; font-size: 5px; white-space: nowrap; }

  /* Envelope back */
  .envelope-back { left: 679px; top: 79px; width: 480px; height: 233px; }
  .envelope-back svg { position: absolute; inset: 0; }
  .envelope-back .brand { position: absolute; left: 0; right: 0; top: 40px; font-size: 10px; color: var(--paper); }
  .envelope-back .brand-dot { width: 18px; height: 18px; background: none; border: 2px solid var(--paper); }

  /* Envelope front */
  .envelope-front { left: 679px; top: 336px; width: 480px; height: 252px; }
  .envelope-front .band { height: 31px; background: var(--navy); }
  .envelope-front .brand { position: absolute; left: 0; right: 0; top: 46px; font-size: 12px; }
  .envelope-front .brand-dot { width: 14px; height: 14px; }
  .envelope-front .mark { position: absolute; left: 322px; top: 70px; width: 130px; height: 130px; }
  .envelope-front .contact { position: absolute; left: 0; right: 0; top: 182px; text-align: center; font-size: 4.4px; white-space: nowrap; }
</style>
</head>
<body>

  <section class="sheet card-front" aria-label="Business card front">
    <div class="brand"><span class="brand-dot"></span>TideForge</div>
  </section>

  <section class="sheet card-back" aria-label="Business card back">
    <div class="band"></div>
    <div class="brand"><span class="brand-dot"></span>TideForge</div>
    <div class="person">
      <p class="name">Desmond K Harlow</p>
      <p class="title">President</p>
    </div>
    <p class="contact">(555) 010-0148 | dharlow4872@mailnest.example | 318 Quillfeather Court Brownsburg, IN 46219</p>
  </section>

  <section class="sheet letterhead" aria-label="Letterhead">
    <div class="band"></div>
    <div class="notch"></div>
    <div class="brand"><span class="brand-dot"></span>TideForge</div>
    <svg class="mark" viewBox="0 0 240 240" aria-hidden="true">
      <circle cx="120" cy="120" r="112" fill="var(--faint)" stroke="var(--faint-line)" stroke-width="6"/>
    </svg>
    <p class="contact">(555) 010-0148 | dharlow4872@mailnest.example | 318 Quillfeather Court Brownsburg, IN 46219</p>
  </section>

  <section class="sheet envelope-back" aria-label="Envelope back">
    <svg viewBox="0 0 480 233" aria-hidden="true">
      <path d="M0 0 H480 V24 L240 100 L0 24 Z" fill="var(--navy)"/>
    </svg>
    <div class="brand"><span class="brand-dot"></span>TideForge</div>
  </section>

  <section class="sheet envelope-front" aria-label="Envelope front">
    <div class="band"></div>
    <div class="brand"><span class="brand-dot"></span>TideForge</div>
    <svg class="mark" viewBox="0 0 150 150" aria-hidden="true">
      <circle cx="75" cy="75" r="68" fill="var(--faint)" stroke="var(--faint-line)" stroke-width="5"/>
    </svg>
    <p class="contact">(555) 010-0148 | dharlow4872@mailnest.example | 318 Quillfeather Court Brownsburg, IN 46219</p>
  </section>

</body>
</html>
```